Cedar Hall businesscard

We changed our name and logo, now we need new business cards.
3-4/72 Marlow Street Kingsford 2032
www.cedarhall-example.org.au
info@cedarhall-example.org.au
Lorna-Jean Whitcombe
Senior Pastor
ph: 02 95874210

```html
<!DOCTYPE html>
<html lang="en">
<head>
<meta charset="utf-8">
<title>Cedar Hall — Business Card</title>
<link rel="stylesheet" href="https://fonts.googleapis.com/css2?family=Open+Sans:wght@400;600;700&display=swap">
<style>
  :root {
    --page-bg: #e9eaec;
    --card-white: #ffffff;
    --pattern-light: #f4f4f5;
    --pattern-mid: #ebebec;
    --brand-blue: #0f6a8f;
    --band-blue-light: #19a6df;
    --band-blue-dark: #0e6f93;
    --silver-light: #f2f2f2;
    --silver-dark: #8f8f91;
    --title-grey: #6a6a6a;
    --text-white: #ffffff;
  }
  * { margin: 0; padding: 0; box-sizing: border-box; }
  html, body {
    width: 1200px; height: 857px; overflow: hidden;
    background: var(--page-bg);
    font-family: "Open Sans", Arial, sans-serif;
  }
  .business-card {
    position: absolute; left: 50px; top: 107px;
    width: 1100px; height: 643px;
    background: var(--card-white);
    overflow: hidden;
  }
  .ornament-field {
    position: absolute; inset: 0;
    background: linear-gradient(120deg, var(--pattern-light), var(--pattern-mid) 60%, var(--pattern-light));
  }
  .brand {
    position: absolute; left: 122px; top: 150px;
    display: flex; align-items: center; gap: 14px;
  }
  .brand-dot {
    width: 26px; height: 26px; border-radius: 50%;
    background: var(--brand-blue); flex: none;
  }
  .brand-name {
    color: var(--brand-blue); font-weight: 600; font-size: 36px;
    line-height: 1; white-space: nowrap;
  }
  .card-swoosh { position: absolute; inset: 0; }
  .person { position: absolute; left: 122px; top: 322px; }
  .person-name { color: var(--brand-blue); font-weight: 700; font-size: 40px; line-height: 1.2; white-space: nowrap; }
  .person-title { color: var(--title-grey); font-weight: 400; font-size: 29px; line-height: 1.3; }
  .contact-top, .contact-bottom {
    position: absolute; right: 68px;
    display: flex; flex-direction: column; align-items: flex-end;
    font-size: 23px; line-height: 36px; white-space: nowrap;
  }
  .contact-top { top: 65px; color: var(--brand-blue); }
  .contact-bottom { top: 516px; color: var(--text-white); }
  .contact-line { display: flex; align-items: center; gap: 10px; }
  .contact-icon { width: 22px; height: 22px; flex: none; }
  .at-sign { font-size: 24px; width: 22px; text-align: center; }
</style>
</head>
<body>
  <div class="business-card">
    <div class="ornament-field" role="img" aria-label="Faint grey decorative swirl pattern background"></div>

    <div class="brand">
      <span class="brand-dot"></span>
      <span class="brand-name">Cedar Hall</span>
    </div>

    <svg class="card-swoosh" width="1100" height="643" viewBox="0 0 1100 643">
      <defs>
        <linearGradient id="bandBlue" x1="0" y1="1" x2="1" y2="0">
          <stop offset="0" stop-color="var(--band-blue-light)"/>
          <stop offset="1" stop-color="var(--band-blue-dark)"/>
        </linearGradient>
        <linearGradient id="silverEdge" x1="0" y1="0" x2="1" y2="0">
          <stop offset="0" stop-color="var(--silver-dark)"/>
          <stop offset="0.45" stop-color="var(--silver-light)"/>
          <stop offset="0.8" stop-color="var(--silver-dark)"/>
          <stop offset="1" stop-color="var(--silver-light)"/>
        </linearGradient>
      </defs>
      <path d="M0 553 C 450 553, 850 440, 1100 240 L1100 284 C 850 470, 450 565, 0 565 Z" fill="url(#silverEdge)"/>
      <path d="M0 563 C 450 563, 850 470, 1100 284 L1100 643 L0 643 Z" fill="url(#bandBlue)"/>
    </svg>

    <div class="person">
      <div class="person-name">Lorna-Jean Whitcombe</div>
      <div class="person-title">Senior Pastor</div>
    </div>

    <div class="contact-top">
      <div class="contact-line">02 95874210
        <svg class="contact-icon" viewBox="0 0 24 24"><path fill="currentColor" d="M6.6 10.8a15.1 15.1 0 0 0 6.6 6.6l2.2-2.2a1 1 0 0 1 1-.25 11.4 11.4 0 0 0 3.6.57 1 1 0 0 1 1 1V20a1 1 0 0 1-1 1A17 17 0 0 1 3 4a1 1 0 0 1 1-1h3.5a1 1 0 0 1 1 1c0 1.25.2 2.45.57 3.57a1 1 0 0 1-.25 1z"/></svg>
      </div>
      <div class="contact-line">info@cedarhall-example.org.au <span class="at-sign">@</span></div>
    </div>

    <div class="contact-bottom">
      <div class="contact-line">3-4/72 Marlow Street Kingsford 2032
        <svg class="contact-icon" viewBox="0 0 24 24"><path fill="currentColor" d="M12 3 1.5 12h3v9h6v-6h3v6h6v-9h3z"/></svg>
      </div>
      <div class="contact-line">www.cedarhall-example.org.au
        <svg class="contact-icon" viewBox="0 0 24 24" fill="none" stroke="currentColor" stroke-width="1.8"><circle cx="12" cy="12" r="9"/><ellipse cx="12" cy="12" rx="4" ry="9"/><path d="M3 12h18M4.5 7.5h15M4.5 16.5h15"/></svg>
      </div>
    </div>
  </div>
</body>
</html>
```